依頼概要
・依頼の目的/概要
人生100年時代に、認知症や介護予防・改善に役立つ、化粧療法レクレーションの表紙デザインをお願いします。

・本の内容
高齢者の皆さんを抱えた、娘さん世代、ソーシャルビジネスとして取り組みたい女性、人の役に立ちたい・介護や医療関係者のスキルアップとして、心を癒すスキンタッチケアとしての化粧療法レクレーションを知って頂き、その効果を実例等で理解する事で、実践してみたくなる内容にしています。またお仕事としても、ボランティアとしても活躍できるセラピストの役割や募集にもふれています。
化粧療法レクレーションがどんなものか?!やるとどんな効果がきたいできるのか?!に、研究データーと実際の実例を交えて説明・解説した本です。

・デザイン要望
美容で心が癒される事が、伝わるようなイメージと解説でもあるので、化粧療法レクレーションのバイブルみたいな感じでしょうか?!(イメージカラーは、ピンクです。http://tkvb.or.jp tkvb-sora.com 色の感じです、参考資料)
もちろん、デザイナーさんのセンスにお任せします。

その他何かご不明な点がございましたら、お気軽にご質問ください。
よろしくお願いいたします。
■ 選んだ理由

認知症や介護の予防・改善を目指した療法ですので、見た方が、明るく安心し、そして楽しみになるイメージが持てるデザインを選びました。特に当選したものは、高齢者と若者が一緒に映る写真の印象が、表題のレクレーションのイメージに繋がるということが、一番の選定理由です。

■ 提案者全員のお礼・コメント

素晴らしい表紙のデザインの応募をいただき、本当に感謝しています。
選定は、本当に悩みました。いくつも表紙にしたい作品がありました。出して頂いた作品が、教科書的と、読み物的な提案を頂いたように思います。皆さん素晴らしかったのですが、今回は親しみやすさを重視させて頂きました。特に最初に応募して頂いた、pelmiさんの表紙には、私の言いたい事が網羅されていて、良かったです。が、今回のテーマを考えて、残念ながら選定致しませんでした。
次の機会に皆様とお仕事ができれば、嬉しいです。ありがとうございました。

```html
<!DOCTYPE html>
<html lang="ja">
<head>
<meta charset="utf-8">
<title>化粧療法レクレーション 表紙</title>
<link rel="stylesheet" href="https://fonts.googleapis.com/css2?family=Noto+Sans+JP:wght@400;500;700&family=Noto+Serif+JP:wght@500;700&display=swap">
<style>
  :root {
    --ink: #1c1c1c;
    --pink: #e8336f;
    --pink-deep: #d92a63;
    --blue: #2a9fd8;
    --sun: #f7ec8e;
    --band-top: #f39ab3;
    --band-bottom: #ee7d9e;
    --white: #ffffff;
  }
  html, body {
    margin: 0;
    padding: 0;
    overflow: hidden;
    background: #f4f4f4;
  }
  .cover {
    position: relative;
    width: 752px;
    height: 1200px;
    overflow: hidden;
    background: var(--white);
    font-family: "Noto Sans JP", sans-serif;
  }
  .portrait-area {
    position: absolute;
    left: 0;
    top: 0;
    width: 752px;
    height: 992px;
    background:
      radial-gradient(ellipse 320px 520px at 90px 430px, #f2e6e6 0%, #f8f1f1 55%, rgba(255,255,255,0) 100%),
      linear-gradient(100deg, #efe3e4 0%, #faf6f6 35%, #ffffff 60%);
  }
  .sun {
    position: absolute;
    left: 325px;
    top: -50px;
    width: 350px;
    height: 350px;
    border-radius: 50%;
    background: radial-gradient(circle, var(--sun) 0%, var(--sun) 62%, rgba(247,236,142,0.55) 85%, rgba(247,236,142,0) 100%);
  }
  .vcol {
    position: absolute;
    margin: 0;
    writing-mode: vertical-rl;
    text-orientation: upright;
    white-space: nowrap;
    line-height: 1;
  }
  .lead {
    left: 667px;
    top: 30px;
    font-size: 46px;
    font-weight: 500;
    color: var(--ink);
  }
  .lead .num { text-orientation: mixed; margin: 6px 0; }
  .purpose {
    left: 570px;
    top: 100px;
    font-size: 40px;
    font-weight: 500;
    color: var(--ink);
  }
  .purpose .key { color: var(--blue); }
  .title {
    left: 449px;
    top: 105px;
    font-size: 62px;
    font-weight: 700;
    color: var(--pink);
  }
  .subcopy {
    font-family: "Noto Serif JP", serif;
    font-weight: 500;
    font-size: 28px;
    color: var(--pink-deep);
  }
  .subcopy-1 { left: 371px; top: 475px; }
  .subcopy-2 { left: 321px; top: 512px; }
  .org {
    left: 695px;
    top: 485px;
    font-size: 19px;
    color: var(--ink);
  }
  .org .latin { text-orientation: mixed; }
  .role {
    left: 662px;
    top: 485px;
    font-size: 20px;
    color: var(--ink);
  }
  .author {
    left: 613px;
    top: 575px;
    font-family: "Noto Serif JP", serif;
    font-size: 38px;
    font-weight: 700;
    color: var(--ink);
    letter-spacing: 2px;
  }
  .message-band {
    position: absolute;
    left: 0;
    top: 992px;
    width: 752px;
    height: 208px;
    background: linear-gradient(180deg, var(--band-top), var(--band-bottom));
    display: flex;
    flex-direction: column;
    align-items: center;
    justify-content: center;
    color: var(--white);
    font-size: 26px;
    font-weight: 500;
    line-height: 46px;
    letter-spacing: 1px;
  }
  .message-band p { margin: 0; }
</style>
</head>
<body>
  <div class="cover">
    <div class="portrait-area" role="img" aria-label="目を閉じた女性の横顔の淡い肌色の写真"></div>
    <div class="sun"></div>

    <div class="vcol lead">人生<span class="num">100</span>年時代に、</div>
    <div class="vcol purpose"><span class="key">認知症</span>や<span class="key">介護予防</span>・<span class="key">改善</span>に役立つ、</div>
    <h1 class="vcol title">「化粧療法レクレーション」</h1>
    <div class="vcol subcopy subcopy-1">「綺麗になる」事が、</div>
    <div class="vcol subcopy subcopy-2">心も脳も元気にしてくれます。</div>

    <div class="vcol org"><span class="latin">NPO</span> 法人 青葉化粧療法レクレーション協会</div>
    <div class="vcol role">代表理事</div>
    <div class="vcol author">春野彩子</div>

    <div class="message-band">
      <p>誰でも、出来る「化粧」です。</p>
      <p>私達、女性にとっては特技ともいえる「化粧」です。</p>
      <p>そんな「化粧」が、自分の愛するお母さんを、</p>
      <p>自分自身の最終章を照らしてくれます。</p>
    </div>
  </div>
</body>
</html>
```